Logo and Business card design!

Welbrook Estates

We are a Property development and real estate company (needs a logo design).

Welbrook estates is based in Sydney Australia and will be dealing with high net worth individuals with a corporate background. The demographic of clients will be relatively youthful and savvy. We do development finance, property development and some portion of property sales

I'd like the 'Welbrook' part of the name to be strength of the title, with 'property' playing a very minor part, perhaps in tiny font somewhere off to the bottom or side or something

Thank you!

Target Market(s)

25-55 years old

Industry/Entity Type

Real Estate Development

Contact Information for Business Card

Please arrange this information as you see fit

Leon Brightwater
Managing Director
0417 582 273
leon@welbrookestates-example.com.au
www.welbrookestates-example.com.au

Logo Text

Welbrook estates

Font styles to use
Serif

Colors

Designer to choose colors to be used in the design.

Requirements
Must have
• PLEASE VIEW THE UPLOADED IMAGES AND EXAMPLES
• And please put 'property' in small letters at the bottom or to the side. I want it to play a minimalist role, with 'WELBROOK' being the feature
• Colours! Please make sure theyre mostly grey and white with possibly some other dark blue and maybe dark grey
Nice to have
• Please feel free to use whatever colors you like, the suggested colors are something I selected momentarily and dont necessarily reflect strict guidelines
Should not have
• NO pictures or shapes of houses. I dont want the logo design to be so literal in its imagery

```html
<!DOCTYPE html>
<html lang="en">
<head>
<meta charset="utf-8">
<title>Welbrook Estates – Business Card</title>
<link rel="stylesheet" href="https://fonts.googleapis.com/css2?family=Josefin+Sans:wght@300&family=Open+Sans:wght@400;700&display=swap">
<style>
  :root {
    --backdrop: #dcdcdc;
    --card-dark: #323335;
    --card-light: #f4f4f4;
    --ink-light: #f2f2f2;
    --ink-dark: #2b2b2b;
    --ink-body: #3a3a3a;
  }
  * { margin: 0; padding: 0; box-sizing: border-box; }
  html, body {
    width: 1200px;
    height: 576px;
    overflow: hidden;
    background: var(--backdrop);
  }
  .sheet {
    position: relative;
    width: 1200px;
    height: 576px;
  }
  .card {
    position: absolute;
    top: 139px;
    width: 484px;
    height: 292px;
    border-radius: 12px;
  }
  .card--front {
    left: 82px;
    background: var(--card-dark);
  }
  .card--back {
    left: 602px;
    background: linear-gradient(135deg, #fafafa 0%, var(--card-light) 55%, #e9e9e9 100%);
  }
  .wordmark {
    position: absolute;
    left: 50%;
    transform: translateX(-50%);
    display: flex;
    align-items: center;
    gap: 10px;
    font-family: "Josefin Sans", sans-serif;
    font-weight: 300;
    white-space: nowrap;
  }
  .wordmark__square {
    width: 30px;
    height: 30px;
    border: 0;
  }
  .wordmark__text {
    display: flex;
    flex-direction: column;
    line-height: 1;
  }
  .wordmark__name {
    font-size: 25px;
    letter-spacing: 2px;
  }
  .wordmark__sub {
    font-size: 12px;
    letter-spacing: 5.2px;
    margin-top: 3px;
  }
  .card--front .wordmark {
    top: 125px;
    color: var(--ink-light);
  }
  .card--front .wordmark__square { background: var(--ink-light); }
  .card--back .wordmark {
    top: 216px;
    color: var(--ink-dark);
  }
  .card--back .wordmark__square { background: var(--ink-dark); }
  .contact {
    position: absolute;
    top: 57px;
    left: 0;
    width: 100%;
    text-align: center;
    font-family: "Open Sans", sans-serif;
    color: var(--ink-body);
  }
  .contact__name {
    font-size: 17px;
    font-weight: 700;
    color: var(--ink-dark);
    line-height: 22px;
  }
  .contact__role {
    font-size: 11px;
    line-height: 16px;
  }
  .contact__phone {
    font-size: 11px;
    line-height: 16px;
    margin-top: 11px;
  }
  .contact__links {
    font-size: 10.5px;
    line-height: 16px;
    margin-top: 2px;
  }
  .contact__divider { margin: 0 6px; }
</style>
</head>
<body>
  <main class="sheet">
    <section class="card card--front" aria-label="Business card front">
      <div class="wordmark">
        <span class="wordmark__square"></span>
        <span class="wordmark__text">
          <span class="wordmark__name">WELBROOK</span>
          <span class="wordmark__sub">ESTATES</span>
        </span>
      </div>
    </section>

    <section class="card card--back" aria-label="Business card back">
      <div class="contact">
        <p class="contact__name">Leon Brightwater</p>
        <p class="contact__role">Managing Director</p>
        <p class="contact__phone">0417 582 273</p>
        <p class="contact__links">leon@welbrookestates-example.com.au<span class="contact__divider">|</span>www.welbrookestates-example.com.au</p>
      </div>
      <div class="wordmark">
        <span class="wordmark__square"></span>
        <span class="wordmark__text">
          <span class="wordmark__name">WELBROOK</span>
          <span class="wordmark__sub">ESTATES</span>
        </span>
      </div>
    </section>
  </main>
</body>
</html>
```